Hackthon event need a Landing Page

We are looking for a landing page to represent an event we are preparing in our country (Dominican Republic), it would be the first of this type, and we want to create a positive impact and make it a brand to make it recurring year to year .

The event is a hackathon where we will be gathering students and professionals to solve challenges using software development.

This landing page should be resposive, multi-language, clean, modern and align with the event logo.

Find a good example of what we are looking for in the following link:

https://brightcodefest.example/

We would like to have the following sections(Not necesarily in this order, not necesarily all of them):

- Brief
- Agenda
- Countdown
- Form Button to redirect to the event registration service.
---> Note: We would like to see the option of having the form in the landing page.
- Contact info and Social Media
- Partners/Sponsors
- Link to intro video

We will be attaching the logo and the variations of colors we are looking to see. It should be with a black background

```html
<!DOCTYPE html>
<html lang="en">
<head>
<meta charset="utf-8">
<title>BrightCode Fest – Software Development Hackathon</title>
<link href="https://fonts.googleapis.com/css2?family=Oswald:wght@400;500;600&family=Poppins:wght@400;500;600&display=swap" rel="stylesheet">
<style>
:root{
  --bg:#1f2023;
  --bg-deep:#17181a;
  --card:#141517;
  --teal:#1fd1b9;
  --coral:#fb877a;
  --coral-deep:#f47a6d;
  --white:#ffffff;
  --muted:#c9c9cc;
  --line:#3a3b3f;
}
*{box-sizing:border-box;margin:0;padding:0}
html,body{width:1200px;height:4732px;overflow:hidden}
body{background:var(--bg);color:var(--white);font-family:"Poppins",sans-serif;position:relative}
.abs{position:absolute}
.oswald{font-family:"Oswald",sans-serif;text-transform:uppercase}

/* header */
.brand{left:88px;top:22px;width:112px;height:100px;display:flex;align-items:center;gap:8px}
.brand-dot{width:18px;height:18px;border-radius:50%;background:var(--coral);flex:none}
.brand-name{font-family:"Oswald",sans-serif;font-size:20px;font-weight:500;line-height:1.05;color:var(--coral)}
.nav{top:50px;font-size:13px;text-transform:uppercase;letter-spacing:.3px}
.btn{background:var(--teal);color:var(--white);font-weight:600;text-transform:uppercase;display:flex;align-items:center;justify-content:center}
.nav-btn{left:947px;top:42px;width:163px;height:39px;font-size:11px}

/* hero */
.hero-photo{left:0;top:0;width:1200px;height:827px;clip-path:polygon(0 0,100% 0,100% 662px,0 827px);
  background:linear-gradient(90deg,#2a2b2e 0%,#3b3c3f 35%,#6a6b6c 60%,#8c8d8b 80%,#5d5e5f 100%)}
.hero-shade{left:0;top:0;width:1200px;height:827px;clip-path:polygon(0 0,100% 0,100% 662px,0 827px);
  background:linear-gradient(90deg,rgba(20,20,22,.75) 0%,rgba(20,20,22,.35) 45%,rgba(20,20,22,0) 70%)}
.hero-date{left:86px;top:262px;font-size:17px}
.hero-title{left:86px;top:294px;font-size:72px;line-height:79px;font-weight:600}
.hero-sub{left:86px;top:548px;font-size:17px;line-height:28px}

/* spectator */
.vline{left:803px;top:781px;width:1px;height:160px;background:var(--teal)}
.illustration{left:165px;top:910px;width:442px;height:377px;border-radius:6px;
  background:radial-gradient(circle at 40% 45%,#2f3036 0%,#25262b 55%,rgba(31,32,35,0) 80%)}
.spec-title{left:673px;top:966px;font-size:41px;line-height:48px;font-weight:500}
.spec-sub{left:673px;top:1132px;font-size:14px;line-height:22px}

.video{left:176px;top:1382px;width:846px;height:491px;
  background:linear-gradient(120deg,#1c2a33 0%,#2d3d48 35%,#4a4239 60%,#1b1d20 100%)}
.play{left:834px;top:1817px;width:112px;height:112px;border-radius:50%;background:var(--teal);display:flex;align-items:center;justify-content:center}

/* about */
.about-photo{left:551px;top:2022px;width:649px;height:551px;
  background:radial-gradient(ellipse at 65% 45%,#4f6e86 0%,#2e4252 40%,rgba(31,32,35,0) 75%)}
.about-title{left:97px;top:2042px;font-size:41px;line-height:48px;font-weight:500}
.about-text{left:97px;top:2155px;width:415px;font-size:13px;line-height:22.3px;color:#e6e6e6}
.about-btn{left:101px;top:2354px;width:121px;height:36px;font-size:11px}

/* countdown */
.count-title{left:0;width:1200px;top:2638px;text-align:center;font-size:41px;font-weight:500}
.count-box{top:2715px;width:116px;height:110px;background:var(--white);color:#111;font-size:54px;display:flex;align-items:center;justify-content:center;font-weight:400}
.count-label{top:2832px;width:116px;text-align:center;font-size:12px;font-weight:500;text-transform:uppercase}
.colon{top:2748px;font-size:30px;font-weight:600;width:42px;text-align:center}

/* agenda */
.section-title{left:0;width:1200px;text-align:center;font-size:41px;font-weight:500}
.agenda-card{top:3051px;width:287px;height:386px;background:var(--card);padding:0 25px}
.agenda-date{margin-top:34px;font-size:10px;color:var(--muted)}
.agenda-day{font-family:"Oswald",sans-serif;font-size:22px;font-weight:500;margin-top:2px;margin-bottom:18px}
.agenda-row{display:flex;font-size:12.5px;color:#d9d9d9;height:45px;align-items:center}
.agenda-row span:first-child{width:150px}
.read-more{display:inline-block;margin-top:8px;color:var(--coral);font-size:12px;font-weight:600;text-decoration:underline}

/* partners */
.partner{width:130px;height:130px;display:flex;flex-direction:column;align-items:center;justify-content:center;gap:14px}
.partner-bar{width:110px;height:4px;background:#e9e9e9}

/* newsletter */
.news{left:90px;top:4045px;width:1020px;height:190px;background:var(--coral)}
.news-title{left:150px;top:4078px;font-size:47px;line-height:50px;font-weight:500}
.news-sub{left:150px;top:4184px;font-size:14px}
.news-input{left:566px;top:4117px;width:360px;height:46px;background:var(--white);color:#666;font-size:13px;display:flex;align-items:center;padding-left:22px;gap:10px}
.news-btn{left:925px;top:4117px;width:123px;height:46px;font-size:12px;border:2px solid var(--white)}

/* footer */
.foot-logo{left:143px;top:4365px;width:184px;height:184px;border-radius:50%;border:3px solid var(--coral);display:flex;align-items:center;justify-content:center;text-align:center}
.social{top:4566px;width:36px;height:36px;border-radius:50%;border:1px solid #55565a}
.foot-head{top:4358px;font-size:20px;font-weight:500}
.foot-links{left:386px;top:4400px;font-size:12px;line-height:26.8px}
.contact{left:568px;font-size:12.5px;line-height:19px}
.contact svg{position:absolute;left:0;top:2px}
.contact div{padding-left:22px}
.field{background:#3a3b3f;color:#cfcfcf;font-size:11px;padding:10px 16px}
.submit{left:800px;top:4569px;width:93px;height:31px;font-size:12px}
.rule{left:90px;top:4668px;width:1020px;height:1px;background:var(--line)}
.copy{left:0;width:1200px;top:4690px;text-align:center;font-size:12px;font-weight:500}
.to-top{left:1131px;top:4648px;width:40px;height:40px;border-radius:50%;background:var(--coral);display:flex;align-items:center;justify-content:center}
</style>
</head>
<body>

<!-- header & hero -->
<div class="abs hero-photo" role="img" aria-label="Team of four professionals gathered around a laptop in a bright office"></div>
<div class="abs hero-shade"></div>

<div class="abs brand"><span class="brand-dot"></span><span class="brand-name">BrightCode<br>Fest</span></div>
<a class="abs nav" style="left:638px">Home</a>
<a class="abs nav" style="left:717px">Agenda</a>
<a class="abs nav" style="left:812px">Countdown</a>
<a class="abs btn nav-btn">Event Registration</a>

<p class="abs hero-date oswald">January 21 - 23, 2022</p>
<h1 class="abs hero-title oswald">Software<br>Development<br>BrightCode</h1>
<p class="abs hero-sub oswald">Gathering students and professionals to solve<br>challenges using software development.</p>

<!-- spectator -->
<div class="abs vline"></div>
<div class="abs illustration" role="img" aria-label="Illustration of a code editor window next to a data report chart"></div>
<h2 class="abs spec-title oswald">Be part of the<br>banking revolution<br>as a spectator</h2>
<p class="abs spec-sub oswald">Watch our live streams on Friday and Sunday via our<br>StreamHub event or here</p>

<div class="abs video" role="img" aria-label="Developer working at a desk with two monitors in a dim room"></div>
<div class="abs play"><svg width="30" height="34" viewBox="0 0 30 34"><path d="M4 2 L28 17 L4 32 Z" fill="#fff"/></svg></div>

<!-- about -->
<div class="abs about-photo" role="img" aria-label="Programmer lit by projected lines of code"></div>
<h2 class="abs about-title oswald">BrightCode join the<br>banking revolution</h2>
<p class="abs about-text">Aenean sollicitudin, lorem quis bibendum auctor, nisi elit consequat ipsum, nec sagittis sem nibh id elit. Duis sed odio sit amet nibh vulputate cursus a sit amet mauris. Morbi accumsan ipsum velit. Nam nec tellus a odio tincidunt auctor a ornare odio. Sed non &nbsp;mauris vitae erat consequat auctor eu in elit. Class aptent taciti sociosqu ad torquent per conubia nostra, per inceptos himenaeos. Mauris in erat justo. Nullam ac urna eu felis…</p>
<a class="abs btn about-btn">Find out more</a>

<!-- countdown -->
<svg class="abs" style="left:0;top:2472px" width="1200" height="436" viewBox="0 0 1200 436"><polygon points="0,0 1200,193 1200,436 0,436" fill="#fb877a"/></svg>
<h2 class="abs count-title oswald">Countdown</h2>
<div class="abs count-box" style="left:305px">01</div>
<div class="abs count-box" style="left:463px">10</div>
<div class="abs count-box" style="left:621px">35</div>
<div class="abs count-box" style="left:779px">22</div>
<div class="abs colon" style="left:421px">:</div>
<div class="abs colon" style="left:579px">:</div>
<div class="abs colon" style="left:737px">:</div>
<div class="abs count-label" style="left:305px">Days</div>
<div class="abs count-label" style="left:463px">Hours</div>
<div class="abs count-label" style="left:621px">Minutes</div>
<div class="abs count-label" style="left:779px">Seconds</div>

<!-- agenda -->
<h2 class="abs section-title oswald" style="top:2972px">BrightCode Agenda</h2>
<div class="abs agenda-card" style="left:151px">
  <p class="agenda-date">21.1.2022</p><p class="agenda-day">DAY 1</p>
  <div class="agenda-row"><span>Team registration</span><span>17:00 – 17:30</span></div>
  <div class="agenda-row"><span>Event kick-off (LS)</span><span>17:30– 18:00</span></div>
  <div class="agenda-row"><span>Introduction of</span><span>18:00 – 18:30</span></div>
  <div class="agenda-row"><span>Hackathon starts</span><span>18:00 – 18:30</span></div>
  <div class="agenda-row"><span>Mentoring 1</span><span>20:00 – 21:00</span></div>
  <a class="read-more">READ MORE</a>
</div>
<div class="abs agenda-card" style="left:456px">
  <p class="agenda-date">21.1.2022</p><p class="agenda-day">DAY 2</p>
  <div class="agenda-row"><span>Team registration</span><span>17:00 – 17:30</span></div>
  <div class="agenda-row"><span>Event kick-off (LS)</span><span>17:30– 18:00</span></div>
  <div class="agenda-row"><span>Introduction of</span><span>18:00 – 18:30</span></div>
  <div class="agenda-row"><span>Hackathon starts</span><span>18:00 – 18:30</span></div>
  <div class="agenda-row"><span>Mentoring 1</span><span>20:00 – 21:00</span></div>
  <a class="read-more">READ MORE</a>
</div>
<div class="abs agenda-card" style="left:759px">
  <p class="agenda-date">21.1.2022</p><p class="agenda-day">DAY 3</p>
  <div class="agenda-row"><span>Team registration</span><span>17:00 – 17:30</span></div>
  <div class="agenda-row"><span>Event kick-off (LS)</span><span>17:30– 18:00</span></div>
  <div class="agenda-row"><span>Introduction of</span><span>18:00 – 18:30</span></div>
  <div class="agenda-row"><span>Hackathon starts</span><span>18:00 – 18:30</span></div>
  <div class="agenda-row"><span>Mentoring 1</span><span>20:00 – 21:00</span></div>
  <a class="read-more">READ MORE</a>
</div>

<!-- partners -->
<h2 class="abs section-title oswald" style="top:3522px">Our Partners</h2>
<div class="abs partner" style="left:238px;top:3620px" role="img" aria-label="Partner badge"><svg width="90" height="70"><rect x="10" y="5" width="70" height="60" fill="none" stroke="#eee" stroke-width="4"/></svg><span class="partner-bar"></span></div>
<div class="abs partner" style="left:534px;top:3620px" role="img" aria-label="Partner badge"><svg width="90" height="80"><circle cx="45" cy="40" r="34" fill="none" stroke="#eee" stroke-width="4"/></svg><span class="partner-bar"></span></div>
<div class="abs partner" style="left:819px;top:3620px" role="img" aria-label="Partner badge"><svg width="90" height="80"><rect x="12" y="8" width="66" height="66" fill="none" stroke="#eee" stroke-width="4"/></svg><span class="partner-bar"></span></div>
<div class="abs partner" style="left:238px;top:3817px" role="img" aria-label="Partner badge"><svg width="90" height="80"><circle cx="45" cy="40" r="34" fill="none" stroke="#eee" stroke-width="4"/></svg><span class="partner-bar"></span></div>
<div class="abs partner" style="left:534px;top:3817px" role="img" aria-label="Partner badge"><svg width="120" height="80"><rect x="15" y="10" width="90" height="60" fill="none" stroke="#eee" stroke-width="4"/></svg><span class="partner-bar"></span></div>
<div class="abs partner" style="left:819px;top:3817px" role="img" aria-label="Partner badge"><svg width="90" height="80"><rect x="12" y="8" width="66" height="66" fill="none" stroke="#eee" stroke-width="4"/></svg><span class="partner-bar"></span></div>

<!-- newsletter -->
<div class="abs news"></div>
<h2 class="abs news-title oswald">Subscribe our<br>newsletter</h2>
<p class="abs news-sub oswald">Join our subscribers list go get the latest news.</p>
<div class="abs news-input"><svg width="16" height="12" viewBox="0 0 16 12"><rect x="0.5" y="0.5" width="15" height="11" fill="none" stroke="#999"/><path d="M1 1 L8 7 L15 1" fill="none" stroke="#999"/></svg>Enter your email address...</div>
<a class="abs btn news-btn">Subscribe</a>

<!-- footer -->
<div class="abs foot-logo"><span class="brand-name" style="font-size:26px">BrightCode<br>Fest</span></div>
<span class="abs social" style="left:171px" aria-label="Social profile"></span>
<span class="abs social" style="left:217px" aria-label="Social profile"></span>
<span class="abs social" style="left:263px" aria-label="Social profile"></span>

<h3 class="abs foot-head oswald" style="left:386px">Helpful links</h3>
<div class="abs foot-links"><p>Home</p><p>Agenda</p><p>Countdown</p><p>Event Registration</p><p>Contact Us</p></div>

<h3 class="abs foot-head oswald" style="left:568px">Contact us</h3>
<div class="abs contact" style="top:4406px"><svg width="14" height="11" viewBox="0 0 14 11"><rect width="14" height="11" fill="#1fd1b9"/><path d="M0 0 L7 6 L14 0" fill="none" stroke="#1f2023"/></svg><div>Email:<br>mail@example.com</div></div>
<div class="abs contact" style="top:4458px"><svg width="13" height="13" viewBox="0 0 24 24"><path d="M6.6 10.8a15 15 0 006.6 6.6l2.2-2.2a1 1 0 011-.25 11 11 0 003.6.6 1 1 0 011 1V20a1 1 0 01-1 1A17 17 0 013 4a1 1 0 011-1h3.5a1 1 0 011 1 11 11 0 00.6 3.6 1 1 0 01-.25 1z" fill="#1fd1b9"/></svg><div>Phone:<br>+08 123 456 7890</div></div>
<div class="abs contact" style="top:4511px"><svg width="12" height="15" viewBox="0 0 12 16"><path d="M6 0a6 6 0 00-6 6c0 4.5 6 10 6 10s6-5.5 6-10a6 6 0 00-6-6zm0 8.5A2.5 2.5 0 116 3.5a2.5 2.5 0 010 5z" fill="#1fd1b9"/></svg><div>Location:<br>Some address line goes<br>here city name</div></div>

<h3 class="abs foot-head oswald" style="left:800px">Get in touch</h3>
<div class="abs field" style="left:800px;top:4408px;width:128px;height:31px">First name</div>
<div class="abs field" style="left:932px;top:4408px;width:125px;height:31px">Last name</div>
<div class="abs field" style="left:800px;top:4450px;width:257px;height:31px">Email</div>
<div class="abs field" style="left:800px;top:4492px;width:257px;height:54px">Message</div>
<a class="abs btn submit">Submit</a>

<div class="abs rule"></div>
<p class="abs copy">© 2022 ALL RIGHTS RESERVED</p>
<a class="abs to-top" aria-label="Back to top"><svg width="14" height="9" viewBox="0 0 14 9"><path d="M1 8 L7 2 L13 8" fill="none" stroke="#fff" stroke-width="2"/></svg></a>

</body>
</html>
```